Podiatry clinic requires a modern revamp and editing of existing website.

I would like a fresh new look and updated information for my current business website. An easy to navigate site with prominent address and phone number for call to action. We are a podiatry clinic that focuses on general and sports podiatry.
I would like 4 pages; including Home page, About Us, Services & Contact.
www.brambleridgefootcare.com

Target Market(s)

Active working professionals.

Industry/Entity Type

Medical

Coding

Coded - Design and coding required

Number of Pages Required

4 page

Font styles to use
Sans Serif

Colors
6b449b

Requirements
Must have
• A modern look with logo and active images; clean and uncluttered. Visible phone number and address for call to action.
• 4 pages - Home, About Us, Services, Contact.
• Home page - update address & service logos.
• About Us - update of personal information.
• Services - Revamp of existing page.
• Contact page to include Google map, email & phone number.
Nice to have
• Ability to add content easily; eg. a blog or adding video onto Home page.
• Link to Facebook page.

```html
<!DOCTYPE html>
<html lang="en">
<head>
<meta charset="utf-8">
<title>Bramble Ridge Foot Care</title>
<link href="https://fonts.googleapis.com/css2?family=Arimo:wght@400;700&family=Open+Sans:wght@400;600&family=Cinzel:wght@400&display=swap" rel="stylesheet">
<style>
:root{
  --purple:#7049b1;
  --purple-deep:#4d2888;
  --purple-text:#5a2fa0;
  --orange:#f6a400;
  --orange-light:#ffc21a;
  --text:#555;
  --muted:#777;
  --white:#fff;
  --rule:#dcdcdc;
  --social:#8e74b8;
}
*{margin:0;padding:0;box-sizing:border-box}
html,body{width:850px;height:1200px;overflow:hidden;background:var(--white)}
body{position:relative;font-family:"Open Sans",sans-serif;color:var(--text)}
.abs{position:absolute}

.site-header{left:0;top:0;width:850px;height:84px;background:var(--purple)}
.brand{left:88px;top:20px;display:flex;align-items:center;gap:8px;color:var(--white)}
.brand-mark{width:30px;height:30px;border:1.5px solid var(--white);border-radius:50%}
.brand-name{font-family:"Cinzel",serif;font-size:17px;line-height:20px;letter-spacing:.5px;white-space:nowrap}
.header-phone{right:98px;top:11px;color:var(--white);font-family:"Arimo",sans-serif;font-size:15px;display:flex;align-items:center;gap:3px}
.main-nav{top:46px;left:379px;font-family:"Arimo",sans-serif;font-size:12px;color:var(--white)}
.main-nav a{color:inherit;text-decoration:none;position:absolute;white-space:nowrap}
.main-nav .active::after{content:"";position:absolute;left:-5px;right:-5px;top:34px;height:2px;background:var(--white)}

.hero{left:0;top:84px;width:850px;height:324px;
  background:linear-gradient(180deg,#c9d8a6 0%,#9bb677 18%,#7f9e5e 34%,#a9ae94 50%,#b9b6a8 66%,#a9a69b 84%,#918f86 100%)}
.hero-title{left:103px;top:187px;width:380px;font-family:"Arimo",sans-serif;font-size:24px;line-height:36px;color:var(--white)}
.hero-dots{left:107px;top:266px;display:flex;gap:3px}
.hero-dots span{width:13px;height:13px;border-radius:50%;background:var(--white)}
.hero-dots span.current{background:transparent;border:2px solid var(--white)}

.intro{left:0;top:408px;width:850px;height:272px;background:linear-gradient(180deg,#fff 35%,#eeeeee 100%)}
.intro-photo{left:490px;top:408px;width:262px;height:272px;
  background:linear-gradient(90deg,rgba(240,236,234,0) 0%,#efd9cf 22%,#e7c3b2 48%,#e6b8a6 62%,#ecd6cc 86%,rgba(240,236,234,0) 100%)}
.intro-title{left:95px;top:450px;font-family:"Arimo",sans-serif;font-weight:400;font-size:24px;color:#444}
.intro-text{left:95px;top:491px;width:395px;font-size:9.3px;line-height:17.2px;color:var(--text)}
.btn-outline{left:96px;top:610px;width:84px;height:24px;border:2px solid var(--orange);color:var(--orange);font-family:"Arimo",sans-serif;font-size:9.5px;display:flex;align-items:center;justify-content:center}

.service{width:220px;text-align:center;top:715px}
.service-photo{width:130px;height:130px;border-radius:50%;margin:0 auto}
.service h2{margin-top:10px;font-family:"Arimo",sans-serif;font-weight:400;font-size:15px;color:var(--purple-text)}
.service p{margin-top:5px;font-size:7.6px;line-height:14px;color:var(--muted)}
.btn-solid{display:inline-flex;align-items:center;justify-content:center;margin-top:7px;width:69px;height:19px;background:linear-gradient(180deg,var(--orange-light),var(--orange));color:var(--white);font-family:"Arimo",sans-serif;font-size:9px}
.divider{top:733px;width:1px;height:206px;background:var(--rule)}

.partners{left:0;top:979px;width:850px;height:84px;border-top:1px solid var(--rule)}
.badge{top:1003px;height:38px;border-radius:4px}

.site-footer{left:0;top:1063px;width:850px;height:137px;background:linear-gradient(180deg,#5a3096,var(--purple-deep))}
.footer-nav{top:1093px;font-family:"Arimo",sans-serif;font-size:10.5px;color:var(--white)}
.copyright{left:100px;top:1116px;font-size:8.5px;color:#d9cdea}
.social{top:1140px;width:24px;height:24px;border-radius:50%;background:var(--social)}
.contact-list{left:527px;top:1085px;color:var(--white);font-size:10px;line-height:21.5px}
.contact-list li{list-style:none;display:flex;align-items:center;gap:8px}
.contact-list svg{width:12px;height:12px;flex:none}
</style>
</head>
<body>
<header class="site-header abs">
  <div class="brand abs"><span class="brand-mark"></span><span class="brand-name">BRAMBLE RIDGE<br>FOOT CARE</span></div>
  <div class="header-phone abs">
    <svg width="12" height="12" viewBox="0 0 24 24"><path fill="#fff" d="M6.6 10.8a15 15 0 0 0 6.6 6.6l2.2-2.2c.3-.3.7-.4 1-.2 1.1.4 2.3.6 3.6.6.6 0 1 .4 1 1V20c0 .6-.4 1-1 1A17 17 0 0 1 3 4c0-.6.4-1 1-1h3.5c.6 0 1 .4 1 1 0 1.3.2 2.5.6 3.6.1.3 0 .7-.2 1z"/></svg>
    1300 555 204
  </div>
  <nav class="main-nav abs">
    <a class="active" style="left:0">HOME</a>
    <a style="left:71px">ABOUT US</a>
    <a style="left:166px">PODIATRY SERVICES</a>
    <a style="left:319px">CONTACT</a>
  </nav>
</header>

<section class="hero abs" role="img" aria-label="Photo of a runner's white and teal shoes walking on a path, green blurred background"></section>
<div class="hero-title abs">Foot Clinic is a Podiatry Clinic in the heart of Melbourne</div>
<div class="hero-dots abs"><span class="current"></span><span></span><span></span><span></span></div>

<section class="intro abs"></section>
<div class="intro-photo abs" role="img" aria-label="Photo of a hand holding a bare foot with heel pain highlighted in red"></div>
<h1 class="intro-title abs">Bramble Ridge Foot Care</h1>
<p class="intro-text abs">Bramble Ridge Foot Care is a Podiatry clinic in the heart of Melbourne CBD. We are located between Queen &amp; Market Streets in the Harbour Lane Business Centre / Rivergate Complex. Our podiatrists are fully qualified health professionals who are able to diagnose, treat, manage or help to prevent all medical conditions that affect the feet and lower limb. We provide General Podiatry Treatment and some Specialised Services in relation to various foot conditions, including Sports Injuries</p>
<div class="btn-outline abs">Read More</div>

<div class="service abs" style="left:90px">
  <div class="service-photo" role="img" aria-label="Photo of a podiatrist in gloves examining a patient's foot" style="background:linear-gradient(135deg,#eef0f3 0%,#e3d2c6 40%,#d6ae97 65%,#b9bcc4 100%)"></div>
  <h2>Podiatry Treatments</h2>
  <p>Proin nulla arcu nonummy luctus dictum eget<br>fermentum et lorem Nunc porta</p>
  <span class="btn-solid">Read More</span>
</div>
<div class="divider abs" style="left:318px"></div>
<div class="service abs" style="left:310px">
  <div class="service-photo" role="img" aria-label="Photo of hands holding a foot bone model" style="background:linear-gradient(135deg,#9ccdc8 0%,#e4c2ad 45%,#d39a80 75%,#b57a66 100%)"></div>
  <h2>Products &amp; Footwear</h2>
  <p>Proin nulla arcu nonummy luctus dictum eget<br>fermentum et lorem Nunc porta</p>
  <span class="btn-solid">Read More</span>
</div>
<div class="divider abs" style="left:529px"></div>
<div class="service abs" style="left:539px;top:714px">
  <div class="service-photo" role="img" aria-label="Photo of a shoe display rack in a store" style="background:linear-gradient(160deg,#e2ddd6 0%,#a89484 35%,#5f4d41 65%,#2f2b2c 100%)"></div>
  <h2>Health &amp; Wellness Products</h2>
  <p>Proin nulla arcu nonummy luctus dictum eget<br>fermentum et lorem Nunc porta</p>
  <span class="btn-solid">Read More</span>
</div>

<section class="partners abs" aria-label="Partners"></section>
<div class="badge abs" role="img" aria-label="Partner badge" style="left:128px;width:142px;background:#d8d4de"></div>
<div class="badge abs" role="img" aria-label="Partner badge" style="left:318px;width:114px;background:#f4d48a"></div>
<div class="badge abs" role="img" aria-label="Partner badge" style="left:484px;width:86px;background:#b8cbe6"></div>
<div class="badge abs" role="img" aria-label="Partner badge" style="left:616px;width:114px;background:#9fd3ab"></div>

<footer class="site-footer abs"></footer>
<div class="footer-nav abs" style="left:100px">HOME</div>
<div class="footer-nav abs" style="left:163px">ABOUT US</div>
<div class="footer-nav abs" style="left:248px">PODIATRY SERVICES</div>
<div class="footer-nav abs" style="left:385px">CONTACT</div>
<div class="copyright abs">© 2016 Company Name&nbsp; All right reserved&nbsp; Term of Use</div>
<div class="social abs" style="left:101px"></div>
<div class="social abs" style="left:131px"></div>
<div class="social abs" style="left:162px"></div>
<div class="social abs" style="left:191px"></div>
<div class="social abs" style="left:220px"></div>
<ul class="contact-list abs">
  <li><svg viewBox="0 0 24 24"><path fill="#fff" d="M12 2a7 7 0 0 0-7 7c0 5 7 13 7 13s7-8 7-13a7 7 0 0 0-7-7zm0 9.5A2.5 2.5 0 1 1 12 6.5a2.5 2.5 0 0 1 0 5z"/></svg>Suite 210 / 75 Harbour Lane Melbourne 3000</li>
  <li><svg viewBox="0 0 24 24"><rect x="2" y="5" width="20" height="14" fill="#fff"/><path d="M2 5l10 8 10-8" fill="none" stroke="#5a3096" stroke-width="1.8"/></svg>info@brambleridgefootcare.com</li>
  <li style="font-size:12.5px"><svg viewBox="0 0 24 24"><path fill="#fff" d="M6.6 10.8a15 15 0 0 0 6.6 6.6l2.2-2.2c.3-.3.7-.4 1-.2 1.1.4 2.3.6 3.6.6.6 0 1 .4 1 1V20c0 .6-.4 1-1 1A17 17 0 0 1 3 4c0-.6.4-1 1-1h3.5c.6 0 1 .4 1 1 0 1.3.2 2.5.6 3.6.1.3 0 .7-.2 1z"/></svg>1300 555 204</li>
</ul>
</body>
</html>
```